WPO Gel Nail Polish Collection for 15 ml bottle

We need a design for our new collection of WPO brand gel nail polish, called "SILK FOG". We are a nail salon / beauty supply distributor selling to retail nail salons in the US. Please look at the sample nail polish bottles attached for your reference. Our bottle will be white with a silver cap. Also, please look at our other project that is on HV for label design for the matching color tip swatches.

Target Market(s)

Retail Nail Salons in the US

Industry/Entity Type

Nail Salon

Colors

Designer to choose colors to be used in the design.

Requirements
Must have
• WPO logo - this needs to be changed to black color for letters WPO and matte gold for the "drop".
• PREMIUM GEL POLISH, SILK FOG, 0.5 oz (15 ml), back label wording.
• Front label wording must be clear and easy to read.
• Dimensions of label must be 1.125" x 4.0".
• Front part of label and back part of label must be spaced correctly so that they will be on opposite sides of the bottle.
Nice to have
• Color stripe possibly where the product name "SILK FOG" will appear, so that it stands out.
Should not have
• no actual pictures of SILK FOG, no overpowering graphics

```html
<!DOCTYPE html>
<html lang="en">
<head>
<meta charset="utf-8">
<title>WPO SILK FOG Gel Polish Label Options</title>
<link rel="stylesheet" href="https://fonts.googleapis.com/css2?family=Lexend:wght@300;500;600&family=Tinos&display=swap">
<style>
  :root {
    --stage-top: #565656;
    --stage-bottom: #7c7c7c;
    --label-paper: #ffffff;
    --label-pattern: #ececec;
    --accent-orange: #f26a21;
    --accent-gold: #c99a2e;
    --ink: #111111;
    --ink-soft: #333333;
  }
  * { margin: 0; padding: 0; box-sizing: border-box; }
  html, body { width: 880px; height: 1200px; overflow: hidden; }
  body {
    position: relative;
    background: linear-gradient(180deg, var(--stage-top), var(--stage-bottom));
    font-family: "Lexend", sans-serif;
    color: var(--ink);
  }
  .label {
    position: absolute;
    left: 38px;
    width: 802px;
    height: 226px;
    background: var(--label-paper);
    border-top: 3px solid var(--accent-orange);
    border-bottom: 3px solid var(--accent-orange);
    box-shadow: 0 18px 22px -14px rgba(0,0,0,0.55);
    overflow: hidden;
  }
  .label-pattern {
    position: absolute; inset: 0;
    background: radial-gradient(ellipse at 50% 50%, var(--label-paper) 10%, var(--label-pattern) 100%);
  }
  .back-copy { position: absolute; left: 56px; top: 0; width: 360px; }
  .back-copy .heading {
    position: absolute; left: 0; white-space: nowrap;
    font-weight: 500; font-size: 14px; letter-spacing: -0.2px;
  }
  .back-copy .body {
    position: absolute; left: 0; width: 360px;
    font-weight: 300; font-size: 9.4px; line-height: 12.2px; color: var(--ink-soft);
  }
  .front { position: absolute; left: 531px; top: 0; width: 200px; height: 100%; text-align: center; }
  .brand {
    position: absolute; left: 0; width: 100%; top: 30px;
    font-weight: 600; font-size: 52px; line-height: 60px; letter-spacing: -2px;
  }
  .brand-dot {
    display: inline-block; width: 12px; height: 12px; border-radius: 50%;
    background: var(--accent-gold); vertical-align: top; margin-top: 12px; margin-left: 3px;
  }
  .product-name {
    position: absolute; font-family: "Tinos", serif; font-size: 32px; line-height: 1;
    white-space: nowrap; text-align: center;
  }
  .tagline, .volume {
    position: absolute; left: 0; width: 100%;
    font-family: "Tinos", serif; color: var(--ink);
  }
  .tagline { font-size: 15.5px; line-height: 17px; }
  .volume { font-size: 12.5px; }
  .stripe-pill {
    left: 38px; top: 106px; width: 200px; height: 46px; border-radius: 23px;
    background: var(--accent-orange); color: #fff; padding-top: 7px;
  }
  .stripe-rect {
    left: 39px; top: 108px; width: 196px; height: 45px;
    background: var(--accent-orange); color: #fff; padding-top: 7px;
  }
  .ring-outline { left: 36px; top: 100px; width: 192px; height: 68px; }
  .ring-outline span, .swoosh span {
    position: absolute; left: 0; width: 100%; top: 17px;
  }
  .ring-outline span { color: var(--ink); }
  .swoosh { left: 48px; top: 108px; width: 180px; height: 58px; }
  .swoosh span { color: #fff; top: 13px; }
  svg { position: absolute; inset: 0; }
</style>
</head>
<body>

<!-- Option 1: rounded stripe -->
<section class="label" style="top:54px">
  <div class="label-pattern" role="img" aria-label="Light grey damask scroll pattern across the label"></div>
  <div class="back-copy">
    <p class="heading" style="top:27px">FOR PROFESSIONAL USE ONLY</p>
    <p class="heading" style="top:55px">DIRECTIONS FOR USE:</p>
    <p class="body" style="top:76px">Apply 1 coat over preferred gel polish base coat. Use magnet to create cat eye design after 2nd coat before curing with LED/UV light. Finish with preferred gel polish top coat. Must cure with LED/UV light after each coat. Approximate cure times: LED 30 seconds; UV 1-2 minutes.</p>
    <p class="heading" style="top:139px">CAUTION:</p>
    <p class="body" style="top:160px">KEEP OUT OF REACH OF CHILDREN. Avoid skin contact. Discontinue use if sensitivity or irritation occurs. Avoid direct sunlight or exposure to extreme heat.</p>
  </div>
  <div class="front">
    <p class="brand">WPO<span class="brand-dot"></span></p>
    <p class="product-name stripe-pill">SILK FOG</p>
    <p class="tagline" style="top:158px">PREMIUM<br>GEL POLISH</p>
    <p class="volume" style="top:198px">0.5 oz (15 ml)</p>
  </div>
</section>

<!-- Option 2: outlined oval -->
<section class="label" style="top:342px">
  <div class="label-pattern" role="img" aria-label="Light grey damask scroll pattern across the label"></div>
  <div class="back-copy">
    <p class="heading" style="top:27px">FOR PROFESSIONAL USE ONLY</p>
    <p class="heading" style="top:55px">DIRECTIONS FOR USE:</p>
    <p class="body" style="top:76px">Apply 1 coat over preferred gel polish base coat. Use magnet to create cat eye design after 2nd coat before curing with LED/UV light. Finish with preferred gel polish top coat. Must cure with LED/UV light after each coat. Approximate cure times: LED 30 seconds; UV 1-2 minutes.</p>
    <p class="heading" style="top:139px">CAUTION:</p>
    <p class="body" style="top:160px">KEEP OUT OF REACH OF CHILDREN. Avoid skin contact. Discontinue use if sensitivity or irritation occurs. Avoid direct sunlight or exposure to extreme heat.</p>
  </div>
  <div class="front">
    <p class="brand">WPO<span class="brand-dot"></span></p>
    <div class="product-name ring-outline">
      <svg viewBox="0 0 192 68" width="192" height="68">
        <ellipse cx="96" cy="34" rx="93" ry="31" fill="none" stroke="var(--accent-orange)" stroke-width="4"/>
        <ellipse cx="98" cy="33" rx="86" ry="26" fill="none" stroke="var(--accent-orange)" stroke-width="1.5"/>
      </svg>
      <span>SILK FOG</span>
    </div>
    <p class="tagline" style="top:180px">PREMIUM GEL POLISH</p>
    <p class="volume" style="top:199px">0.5 oz (15 ml)</p>
  </div>
</section>

<!-- Option 3: square stripe -->
<section class="label" style="top:626px">
  <div class="label-pattern" role="img" aria-label="Light grey damask scroll pattern across the label"></div>
  <div class="back-copy">
    <p class="heading" style="top:27px">FOR PROFESSIONAL USE ONLY</p>
    <p class="heading" style="top:55px">DIRECTIONS FOR USE:</p>
    <p class="body" style="top:76px">Apply 1 coat over preferred gel polish base coat. Use magnet to create cat eye design after 2nd coat before curing with LED/UV light. Finish with preferred gel polish top coat. Must cure with LED/UV light after each coat. Approximate cure times: LED 30 seconds; UV 1-2 minutes.</p>
    <p class="heading" style="top:139px">CAUTION:</p>
    <p class="body" style="top:160px">KEEP OUT OF REACH OF CHILDREN. Avoid skin contact. Discontinue use if sensitivity or irritation occurs. Avoid direct sunlight or exposure to extreme heat.</p>
  </div>
  <div class="front">
    <p class="brand">WPO<span class="brand-dot"></span></p>
    <p class="product-name stripe-rect">SILK FOG</p>
    <p class="tagline" style="top:167px">PREMIUM GEL POLISH</p>
    <p class="volume" style="top:199px">0.5 oz (15 ml)</p>
  </div>
</section>

<!-- Option 4: oval with gold rim -->
<section class="label" style="top:914px">
  <div class="label-pattern" role="img" aria-label="Light grey damask scroll pattern across the label"></div>
  <div class="back-copy">
    <p class="heading" style="top:27px">FOR PROFESSIONAL USE ONLY</p>
    <p class="heading" style="top:55px">DIRECTIONS FOR USE:</p>
    <p class="body" style="top:76px">Apply 1 coat over preferred gel polish base coat. Use magnet to create cat eye design after 2nd coat before curing with LED/UV light. Finish with preferred gel polish top coat. Must cure with LED/UV light after each coat. Approximate cure times: LED 30 seconds; UV 1-2 minutes.</p>
    <p class="heading" style="top:139px">CAUTION:</p>
    <p class="body" style="top:160px">KEEP OUT OF REACH OF CHILDREN. Avoid skin contact. Discontinue use if sensitivity or irritation occurs. Avoid direct sunlight or exposure to extreme heat.</p>
  </div>
  <div class="front">
    <p class="brand">WPO<span class="brand-dot"></span></p>
    <div class="product-name swoosh">
      <svg viewBox="0 0 180 58" width="180" height="58">
        <ellipse cx="88" cy="30" rx="88" ry="27" fill="var(--accent-gold)"/>
        <ellipse cx="92" cy="28" rx="86" ry="26" fill="var(--accent-orange)"/>
      </svg>
      <span>SILK FOG</span>
    </div>
    <p class="tagline" style="top:181px">PREMIUM GEL POLISH</p>
    <p class="volume" style="top:199px">0.5 oz (15 ml)</p>
  </div>
</section>

</body>
</html>
```